Web site - 5-8 page

We are a small, fresh pasta business called The Noodle Baroness located in suburbs of Sacramento, CA. We sell our pasta, ravioli, meatballs and sauce at farmer's markets, events, and soon in our café & marketplace. (Jan 2014) . We also provide catering services. The site needs to communicate FRESH, local, no preservatives, artisan quality pasta. We offer vegetarian, vegan and gluten free products as well.

We would like a web site using our logos and colors to feature what we do, and where people can come buy it. A page to our standard take and make items/menu, our seasonal take and make menu, our catering menu, our new hot food café menu.

We want a page that we can update with "Where can you find The Noodle Baroness"
A "specials page" and a page they can order from that they choose the location to pick it up or in the delivery area we deliver to them.
A page with photo's and referrals, testimony, comments, about us, etc. Maybe a page for recipes.
We need to update the events/find us page all the time, weekly, so it needs to be easy for us to go in and do that. We are Window's (not MAC) users if that makes a difference or not, not sure.

Ideally, the same person(s) that make the website would also do a separate project creating our catering and hot food menu brochure/layout and recipe cards
Updates

I would like to see the landing page have the pasta shapes/sizes element that is found in the refrigerator wrap, the wrap on the trailer, and the menu - see photo and uploads. It's used as a banner or as a background, bright green.

                                   

 

Would like visitors to be able to "like" me or follow me from my web page. A button or a link?

                                        http://www.brightlarder-example.com/our-food/

Really like the layout of this site. More grocery oriented than café, but we are a take and make marketplace as well as a Panini salads and hot pasta menu for lunch.

Please add Café + Marketplace to headers. Our logo is good but we are now adding a café element and a fresh marketplace, se we need to communicate what we are/what we do. We think adding Café + Marketplace as a descriptor will help. Any ideas, feel free to put your own spin on it. Thank you!!

The designs are good...thanks to everyone!

Target Market(s)

#1, busy mom's, busy family's (FAST, Economical meals, no preservatives, local food)
#2 24-34 yr olds that want fresh, vegetarian, vegan or gluten free meal options (no preservatives, local food)
#3 Fresh pasta lovers - any age. The enjoyment of quality fresh pasta and a good meal experience sharing it with friends and family

Industry/Entity Type

Catering

Font styles to use
Other font styles liked:
• EideticNeoRegular, duffy

Colors
9bcb3c
f78f20
eb1f27

Requirements
Must have
• Address, phone, name, logo, colors
Fresh pasta, ravioli, sauce and meatballs in take and make convenient packages. Stress fresh, preservative free, local ingredients, cooks in 45 SECONDS to 3.5 minutes depending on the pasta cut.
FAST meal
Where to find us page - upcoming events
A "specials" page
A page for recipe, how to cook our pasta, how to freeze and store fresh pasta,
How to order online page
Nice to have
• Testimony, links to Chatterbook, chirpnet, etc. Place for photo's of product, recent events, customer comments on how they used the product to create their recipe.
Should not have
• No stock photo's of tomato's, no dried pasta images, no Italian flags. No cheesy old world Italian loo or feel. Think fresh, modern, FAST!

```html
<!DOCTYPE html>
<html lang="en">
<head>
<meta charset="utf-8">
<title>The Noodle Baroness — Home</title>
<link href="https://fonts.googleapis.com/css2?family=Gochi+Hand&family=Arimo:wght@400;700&display=swap" rel="stylesheet">
<style>
:root{
  --green:#9bcb3c;
  --orange:#f78f20;
  --red:#eb1f27;
  --ink:#1a1a1a;
  --grey:#777;
  --rule:#bdbdbd;
  --hand:"Gochi Hand", cursive;
  --sans:"Arimo", Arial, sans-serif;
}
*{box-sizing:border-box;margin:0;padding:0}
html,body{width:1200px;height:1042px;overflow:hidden;background:#fff}
body{font-family:var(--sans);color:var(--ink)}
.page{position:relative;width:1200px;height:1042px}
.abs{position:absolute}
a{color:inherit;text-decoration:none}

/* header */
.brand{left:248px;top:52px;width:130px;font-family:var(--hand);font-size:26px;line-height:26px;color:var(--red);display:flex;gap:8px;align-items:flex-start}
.brand-dot{width:12px;height:12px;border-radius:50%;background:var(--orange);margin-top:8px;flex:none}
.utility{top:28px;display:flex;flex-direction:column;align-items:center;font-size:12px;width:50px}
.utility svg{width:28px;height:28px;margin-bottom:4px}
.u-search{left:796px;color:var(--orange)}
.u-cart{left:855px;color:var(--green)}
.u-login{left:909px;color:var(--red)}
.main-nav{left:387px;top:96px;width:566px;display:flex;justify-content:space-between;font-family:var(--hand);font-size:21px;color:var(--grey)}
.main-nav .current{color:var(--red)}

/* hero */
.hero{left:250px;top:144px;width:700px;height:242px;border:1px solid #ddd;border-radius:4px;overflow:hidden;background:linear-gradient(90deg,#fbf6ee 0%,#f6ebd9 45%,#efdcc2 100%)}
.hero-photo{position:absolute;left:262px;top:0;width:438px;height:242px;background:radial-gradient(ellipse at 60% 60%,#f3dc8e 0%,#e8c677 35%,#b06a3a 62%,rgba(240,224,200,0) 80%)}
.hero-title{position:absolute;left:36px;top:48px;font-family:var(--hand);font-size:40px;line-height:40px;color:var(--red)}
.hero-price{position:absolute;left:36px;top:86px;font-family:var(--hand);font-size:20px;color:var(--red)}
.hero-copy{position:absolute;left:36px;top:116px;width:200px;font-size:10px;line-height:14.4px}
.btn{display:inline-block;background:var(--red);color:#fff;font-weight:700;font-size:10px;text-align:center;border-radius:2px;box-shadow:0 2px 0 #9c1218}
.hero .btn{position:absolute;left:36px;top:170px;width:130px;height:24px;line-height:24px}
.dots{left:565px;top:398px;display:flex;gap:7.5px}
.dots i{width:11px;height:11px;border-radius:50%;background:#999}
.dots i.on{background:var(--orange)}

/* tiles */
.tile{border-radius:3px;overflow:hidden}
.holiday{left:250px;top:422px;width:216px;height:288px;background:var(--green)}
.holiday h2{position:absolute;top:12px;width:100%;text-align:center;font-family:var(--hand);font-weight:400;font-size:29px;line-height:27px;color:#fff}
.holiday-photo{position:absolute;left:0;top:78px;width:216px;height:100px;background:radial-gradient(ellipse at 50% 70%,#f4ecd7 0%,#e6dcc2 50%,#cfd0c8 75%,var(--green) 100%)}
.badge{position:absolute;left:74px;top:72px;width:68px;height:68px;border-radius:50%;background:var(--orange);border:3px solid #fff;color:#fff;font-family:var(--hand);font-size:14px;line-height:14px;text-align:center;padding-top:9px}
.badge b{display:block;font-size:20px;font-weight:400;line-height:18px}
.schedule{position:absolute;left:8px;top:164px;width:202px;height:98px;background:rgba(255,255,255,.85);border-radius:4px}
.schedule .col{position:absolute;top:6px;width:96px;text-align:center}
.schedule .col:first-child{left:2px}
.schedule .col:last-child{left:104px}
.schedule h3{font-size:17px;color:#333;margin-bottom:6px}
.schedule p{font-size:10px;font-weight:700;color:#555;line-height:14.5px}
.holiday .btn{position:absolute;left:37px;top:251px;width:143px;height:23px;line-height:23px}

.hours{left:491px;top:422px;width:217px;height:133px;background:var(--orange);color:#fff;text-align:center}
.hours h2{margin-top:22px;font-size:29px;line-height:30px}
.hours p{font-size:20px;line-height:24px}
.hours strong{display:block;font-family:var(--hand);font-weight:400;font-size:30px;line-height:32px}

.menu-dl{left:733px;top:422px;width:217px;height:133px;background:linear-gradient(135deg,#f05a62,#e0303a 60%,#f27b80)}
.doc{position:absolute;left:23px;top:26px;width:68px;height:80px;background:#fff;border-radius:2px;box-shadow:2px 3px 6px rgba(0,0,0,.3)}
.menu-dl h3{position:absolute;left:100px;top:24px;width:114px;font-family:var(--hand);font-weight:400;font-size:12px;line-height:15px;color:#fff;white-space:nowrap}
.menu-dl .btn{position:absolute;left:101px;top:81px;width:72px;height:24px;line-height:24px;border:1px solid #fff}

.rewards{left:491px;top:578px;width:217px;height:132px;background:linear-gradient(180deg,#f2d6c8,#d9a98f 60%,#8d6a5c)}
.rewards-veil{position:absolute;left:20px;top:18px;width:177px;height:72px;background:rgba(255,255,255,.75);border-radius:6px}
.rewards h2{position:absolute;top:14px;width:100%;text-align:center;font-family:var(--hand);font-weight:400;font-size:27px;color:var(--red)}
.rewards p{position:absolute;top:50px;width:100%;text-align:center;font-size:9.6px;line-height:12px}
.rewards .btn{position:absolute;left:78px;top:94px;width:64px;height:23px;line-height:23px}

.video{left:733px;top:578px;width:217px;height:132px;background:radial-gradient(ellipse at 55% 45%,#e79a3a 0%,#c9542a 35%,#eaeaea 70%,#d8d4e6 100%)}
.play{position:absolute;left:82px;top:39px;width:54px;height:54px;border-radius:50%;background:rgba(20,20,20,.85)}
.play:after{content:"";position:absolute;left:22px;top:16px;border-left:16px solid #fff;border-top:11px solid transparent;border-bottom:11px solid transparent}
.video p{position:absolute;bottom:4px;width:100%;text-align:center;font-family:var(--hand);font-size:21px;color:var(--ink)}

/* products */
.product{top:748px;height:104px}
.product h3{position:absolute;right:8px;top:0;font-family:var(--hand);font-weight:400;font-size:18px;white-space:nowrap}
.product .price{position:absolute;right:8px;top:22px;font-family:var(--hand);font-size:14px;color:var(--red);white-space:nowrap}
.product .shot{position:absolute;border-radius:50%}
.product .btn{position:absolute;right:8px;top:80px;width:47px;height:14px;line-height:14px;font-weight:400;font-size:9px}
.p1{left:240px;width:179px}
.p2{left:419px;width:179px}
.p3{left:598px;width:180px}
.p1 .shot{left:4px;top:38px;width:118px;height:76px;background:radial-gradient(ellipse,#d4a65a 0%,#8aa66a 40%,#eef0f0 70%,rgba(255,255,255,0) 100%)}
.p2 .shot{left:8px;top:42px;width:104px;height:58px;background:radial-gradient(ellipse,#f2df8c 0%,#e6cd6e 50%,rgba(255,255,255,0) 100%)}
.p3 .shot{left:4px;top:40px;width:128px;height:64px;background:radial-gradient(ellipse,#f2e3a6 0%,#e8d38c 55%,rgba(255,255,255,0) 100%)}
.divider{top:748px;width:1px;height:102px;background:var(--rule)}
.signup{left:778px;top:748px;width:176px;text-align:center}
.signup h3{font-family:var(--hand);font-weight:400;font-size:19px;line-height:27px}
.signup form{display:flex;margin:6px 0 0 14px}
.signup input{width:129px;height:19px;border:1px solid #ccc;font:10px var(--sans);padding:0 6px;color:#888}
.signup button{width:21px;height:19px;border:0;background:var(--red);color:#fff;font:10px var(--sans)}

/* social strip */
.rule{left:261px;width:673px;height:1px;background:#999}
.chirp-mark{left:270px;top:912px;width:20px;height:20px;border-radius:50%;background:var(--red)}
.tweet{left:302px;top:906px;width:330px;font-size:10px;line-height:14.4px}
.tweet a{color:var(--red)}
.social-row{right:266px;top:914px;display:flex;align-items:center;gap:12px;font-size:10px;white-space:nowrap}
.social-links{font-weight:700;color:var(--red)}
.social-links span{margin:0 8px}
.like{display:flex;font-size:8px}
.like b{border:1px solid #aab3c7;background:#eef0f5;color:#3b4f80;padding:1px 5px;border-radius:2px}
.like i{font-style:normal;border:1px solid #ccc;padding:1px 4px;margin-left:4px}

.footer-nav{left:0;top:970px;width:1195px;text-align:center;font-size:10px}
.footer-nav a{margin:0 6px}
.footer-nav em{font-style:normal}
.copyright{left:0;top:994px;width:1195px;text-align:center;font-size:10px;font-weight:700}
</style>
</head>
<body>
<div class="page">

  <header>
    <a class="brand abs" href="#"><span class="brand-dot"></span><span>The Noodle Baroness</span></a>

    <a class="utility u-search abs" href="#">
      <svg viewBox="0 0 28 28" fill="none" stroke="currentColor" stroke-width="4" stroke-linecap="round"><circle cx="12" cy="11" r="7"/><line x1="17" y1="17" x2="23" y2="25"/></svg>search</a>
    <a class="utility u-cart abs" href="#">
      <svg viewBox="0 0 28 28" fill="none" stroke="currentColor" stroke-width="3.5" stroke-linejoin="round"><path d="M1 5h4l3 14h15l3-11H8"/></svg>cart</a>
    <a class="utility u-login abs" href="#">
      <svg viewBox="0 0 28 28" fill="none" stroke="currentColor" stroke-width="3"><circle cx="14" cy="14" r="12"/><circle cx="14" cy="11" r="4.5" fill="currentColor"/><path d="M6 22c3-5 13-5 16 0" fill="currentColor"/></svg>login</a>

    <nav class="main-nav abs">
      <a class="current" href="#">Home</a><a href="#">About Us</a><a href="#">Specials</a><a href="#">order online</a><a href="#">Recipe</a><a href="#">Testimonials</a><a href="#">Find Us</a>
    </nav>
  </header>

  <section class="hero abs">
    <div class="hero-photo" role="img" aria-label="Fresh tagliatelle with basil, tomato and mozzarella in a wooden bowl"></div>
    <h1 class="hero-title">Fresh Pasta</h1>
    <p class="hero-price">12 oz. $6.00 &amp; up</p>
    <p class="hero-copy">Available as angel hair, spaghetti, linguini, fettuccine, tagliatini, pappardelle, penne, rigatoni, sheets or shells.</p>
    <a class="btn" href="#">see more weekly deals</a>
  </section>
  <div class="dots abs"><i class="on"></i><i></i><i></i><i></i></div>

  <section class="tile holiday abs">
    <h2>Holiday Meals<br>Made Easy</h2>
    <div class="holiday-photo" role="img" aria-label="Plate of ravioli with herbs"></div>
    <div class="badge">click<b>&amp;</b>pick up</div>
    <div class="schedule">
      <div class="col"><h3>Pick Up</h3><p>NOVEMBERE 21<br>NOVEMBERE 22<br>NOVEMBERE 24</p></div>
      <div class="col"><h3>Order By</h3><p>NOVEMBERE 21<br>NOVEMBERE 22<br>NOVEMBERE 24</p></div>
    </div>
    <a class="btn" href="#">order yours now</a>
  </section>

  <section class="tile hours abs">
    <h2>Store Hours</h2>
    <p>Thanksgiving Day</p>
    <strong>7am - 5pm</strong>
  </section>

  <section class="tile menu-dl abs">
    <div class="doc"></div>
    <h3>The Noodle Baroness<br>Fall Seasonal<br>Menu 2013</h3>
    <a class="btn" href="#">download</a>
  </section>

  <section class="tile rewards abs" role="img" aria-label="Group of happy friends laughing together">
    <div class="rewards-veil"></div>
    <h2>Friends rewards</h2>
    <p>Receive Weekly Coupons<br>Get Bonus Point Coupons<br>Earn to Convert to Cash Rewards</p>
    <a class="btn" href="#">join now</a>
  </section>

  <section class="tile video abs" role="img" aria-label="Bowl of gnocchi in tomato sauce with basil">
    <span class="play"></span>
    <p>watch our latest tv ad</p>
  </section>

  <article class="product p1 abs">
    <div class="shot" role="img" aria-label="Dish of penne with spinach"></div>
    <h3>FRESH PASTA</h3><p class="price">12 oz. $6.00 &amp; UP</p>
    <a class="btn" href="#">Buy</a>
  </article>
  <div class="divider abs" style="left:419px"></div>
  <article class="product p2 abs">
    <div class="shot" role="img" aria-label="Fresh ravioli with parsley and capers"></div>
    <h3>FRESH RAVIOLI</h3><p class="price">12 oz. $8.00 &amp; UP</p>
    <a class="btn" href="#">Buy</a>
  </article>
  <div class="divider abs" style="left:598px"></div>
  <article class="product p3 abs">
    <div class="shot" role="img" aria-label="Pile of fresh gnocchi"></div>
    <h3>FRESH GNOCCHI</h3><p class="price">12 oz. $7.00 &amp; UP</p>
    <a class="btn" href="#">Buy</a>
  </article>
  <div class="divider abs" style="left:778px"></div>
  <section class="signup abs">
    <h3>SIGN - UP FOR<br>LATEST OFFERS</h3>
    <form><input type="text" value="Enter post code or town"><button type="button">GO</button></form>
  </section>

  <div class="rule abs" style="top:886px"></div>
  <span class="chirp-mark abs"></span>
  <p class="tweet abs">Have you booked your Christmas party yet? Celebrate in classic Italian style at one of our restaurants! <a href="#">http://chirp.example/5Ugroe6rbe</a></p>
  <div class="social-row abs">
    <p class="social-links"><a href="#">Chirpnet</a><span>I</span><a href="#">Chatterbook</a></p>
    <p class="like"><b>Like</b><i>117</i></p>
  </div>
  <div class="rule abs" style="top:958px"></div>

  <nav class="footer-nav abs">
    <a href="#">Home</a><em>•</em><a href="#">About Us</a><em>•</em><a href="#">Specials</a><em>•</em><a href="#">Order Online</a><em>•</em><a href="#">Recipe</a><em>•</em><a href="#">Testimonials</a><em>•</em><a href="#">Find Us</a>
  </nav>
  <p class="copyright abs">© 2013 The Noodle Baroness.</p>

</div>
</body>
</html>
```